Retail swing tag labels for a sale / reduction

We need some graphics done to be made into retail swing tag labels, for the purpose of reductions on selected products.

We have attached 2 examples of previous designs that were similar idea, but more themed for 'autumn' and 'winter'. This theme will just have the word 'REDUCED'.

The white areas can be smaller in size, as we would like to include a large "20% OFF" at the bottom, and then a 30%, 40%, 50% option.

Overall colour scheme should be red background with some form of detailed patterning (see previous examples). Bright and e-catching.

Any other questions, just ask.

The screenshot is front the printers, but in horizontal orientation.

The finished dimensions will be A6 portrait, printed both sides.

We have also included the vector file of the shop "Hallmere Furnishings", which can be included on 1 of the sides.

```html
<!DOCTYPE html>
<html lang="en">
<head>
<meta charset="utf-8">
<title>Reduced – Swing Tags</title>
<link rel="stylesheet" href="https://fonts.googleapis.com/css2?family=Bebas+Neue&family=Josefin+Sans:wght@400&display=swap">
<style>
  :root {
    --red: #f03a3c;
    --red-deep: #c8161f;
    --red-dark: #a5111a;
    --maroon: #5e0f1b;
    --maroon-mid: #7a1422;
    --coral: #e8403f;
    --crimson: #c42026;
    --gold: #c9a46a;
    --white: #ffffff;
    --page: #ffffff;
  }
  * { box-sizing: border-box; margin: 0; padding: 0; }
  html, body { width: 1200px; height: 1137px; overflow: hidden; background: var(--page); }
  .canvas { position: relative; width: 1200px; height: 1137px; }

  .tag {
    position: absolute;
    overflow: hidden;
    box-shadow: 0 1px 4px rgba(0,0,0,0.18);
  }
  .tag--front {
    left: 63px; top: 198px; width: 515px; height: 728px;
    background:
      radial-gradient(ellipse at 55% 35%, #ff4a4a 0%, var(--red) 45%, var(--red-deep) 100%);
  }
  .tag--back {
    left: 617px; top: 200px; width: 513px; height: 725px;
    background: linear-gradient(180deg, var(--red-dark) 0%, #e23337 30%, #f0595a 52%, #fbd0d0 74%, var(--white) 90%);
  }

  .pattern-area { position: absolute; inset: 0; }

  .string {
    position: absolute; top: 0; width: 1.5px; background: rgba(255,255,255,0.85);
  }

  .badge {
    position: absolute;
    border-radius: 50%;
    display: flex; flex-direction: column; align-items: center; justify-content: center;
    font-family: "Bebas Neue", sans-serif;
    line-height: 0.85;
    transform: translate(-50%, -50%);
  }
  .badge .pct { display: block; }
  .badge .off { display: block; }
  .badge--gold { background: var(--gold); color: var(--maroon); }
  .badge--white { background: var(--white); color: var(--maroon); }
  .badge--maroon { background: var(--maroon); color: var(--white); }
  .badge--coral { background: var(--coral); color: var(--maroon); }
  .badge--crimson { background: var(--crimson); color: var(--white); }

  .headline {
    position: absolute;
    font-family: "Bebas Neue", sans-serif;
    color: var(--white);
    -webkit-text-stroke: 2px var(--gold);
    paint-order: stroke fill;
    line-height: 1;
    white-space: nowrap;
  }
  .tag--front .headline {
    left: 257px; top: 383px;
    font-size: 132px;
    transform: translate(-50%, -50%) rotate(-15deg);
    text-shadow: 10px 10px 0 var(--red-dark);
  }
  .tag--back .headline {
    left: 66px; top: 32px;
    font-size: 150px;
    letter-spacing: 1px;
  }

  .price-box {
    position: absolute; left: 64px; width: 284px;
    background: var(--white);
    border: 3px solid var(--gold);
    border-radius: 6px;
    font-family: "Bebas Neue", sans-serif;
    font-size: 38px;
    line-height: 1;
    padding: 8px 12px;
  }
  .price-box--was { top: 172px; height: 61px; color: var(--gold); }
  .price-box--now { top: 240px; height: 118px; color: var(--red-dark); }

  .hero-discount {
    position: absolute; left: 200px; top: 477px;
    width: 194px; height: 194px;
    transform: translate(-50%, -50%);
    border-radius: 50%;
    background: var(--maroon-mid);
    border: 4px solid var(--gold);
    box-shadow: inset 0 0 0 5px var(--white), 0 3px 8px rgba(0,0,0,0.25);
    display: flex; flex-direction: column; align-items: center; justify-content: center;
    font-family: "Bebas Neue", sans-serif;
    color: var(--white);
    line-height: 0.85;
  }
  .hero-discount .pct { font-size: 86px; }
  .hero-discount .off { font-size: 56px; }

  .brand-mark {
    position: absolute;
    border: 1.5px solid currentColor;
  }
  .brand-name {
    position: absolute;
    font-family: "Josefin Sans", sans-serif;
    font-weight: 400;
    text-transform: uppercase;
    white-space: nowrap;
    transform: translateX(-50%);
  }
  .tag--front .brand-mark { left: 223px; top: 550px; width: 70px; height: 70px; color: var(--white); }
  .tag--front .brand-name { left: 258px; top: 660px; font-size: 25px; letter-spacing: 3px; color: var(--white); }
  .tag--back .brand-mark { left: 197px; top: 606px; width: 50px; height: 50px; color: var(--maroon-mid); }
  .tag--back .brand-name { left: 222px; top: 678px; font-size: 18px; letter-spacing: 2px; color: var(--maroon-mid); }
</style>
</head>
<body>
<div class="canvas">

  <section class="tag tag--front">
    <div class="pattern-area" role="img" aria-label="Radiating burst rays with halftone dot pattern in red tones"></div>

    <span class="string" style="left:76px;height:150px"></span>
    <span class="string" style="left:124px;height:210px"></span>
    <span class="string" style="left:147px;height:90px"></span>

    <div class="badge badge--gold" style="left:146px;top:120px;width:72px;height:72px">
      <span class="pct" style="font-size:30px">30%</span><span class="off" style="font-size:17px">OFF</span>
    </div>
    <div class="badge badge--white" style="left:77px;top:181px;width:78px;height:78px">
      <span class="pct" style="font-size:32px">40%</span><span class="off" style="font-size:18px">OFF</span>
    </div>
    <div class="badge badge--maroon" style="left:129px;top:250px;width:100px;height:100px">
      <span class="pct" style="font-size:34px">50%</span><span class="off" style="font-size:19px">OFF</span>
    </div>

    <h1 class="headline">REDUCED</h1>

    <span class="brand-mark"></span>
    <p class="brand-name">Hallmere Furnishings</p>
  </section>

  <section class="tag tag--back">
    <div class="pattern-area" role="img" aria-label="Faint radiating rays and halftone dots fading from red to white"></div>

    <h2 class="headline">REDUCED</h2>

    <div class="price-box price-box--was">WAS</div>
    <div class="price-box price-box--now">NOW</div>

    <div class="hero-discount">
      <span class="pct">20%</span><span class="off">OFF</span>
    </div>

    <span class="string" style="left:387px;top:140px;height:380px"></span>
    <span class="string" style="left:429px;top:140px;height:430px"></span>
    <span class="string" style="left:458px;top:140px;height:305px"></span>

    <div class="badge badge--gold" style="left:456px;top:481px;width:80px;height:80px">
      <span class="pct" style="font-size:32px">30%</span><span class="off" style="font-size:18px">OFF</span>
    </div>
    <div class="badge badge--coral" style="left:390px;top:546px;width:78px;height:78px">
      <span class="pct" style="font-size:32px">40%</span><span class="off" style="font-size:18px">OFF</span>
    </div>
    <div class="badge badge--crimson" style="left:441px;top:609px;width:102px;height:102px">
      <span class="pct" style="font-size:34px">50%</span><span class="off" style="font-size:19px">OFF</span>
    </div>

    <span class="brand-mark"></span>
    <p class="brand-name">Hallmere Furnishings</p>
  </section>

</div>
</body>
</html>
```